Business card design needed

Business Card design required for new small plumbing business.
Would like a logo/text look that is simple and unique and does not have to be representative of a plumbing company (ie. having a cartoon plumber or toilet etc) as the companyname is self explanatory.
Would like the main colour to be green (lime green).
Updates

Industry/Entity Type

Plumber

Contact Information for Business Card

BRAVELL PLUMBING
ABN 61 904 127 558 003

Trevor Hasketh
Licensed Plumber 83615
Phone: 0412 870 245

27 Bravell Drive,
Fernhollow. 3987 Westmark

Email: bravellplumbing@mailnest.example

Logo Text

Bravell Plumbing

Logo styles of interest
Character Logo
Wordmark Logo
Lettermark Logo

```html
<!DOCTYPE html>
<html lang="en">
<head>
<meta charset="utf-8">
<title>Bravell Plumbing – Business Card</title>
<link rel="stylesheet" href="https://fonts.googleapis.com/css2?family=Crimson+Text:wght@400&family=Open+Sans:wght@300;400&display=swap">
<style>
  :root {
    --lime: #4cb83a;
    --lime-dark: #23701b;
    --navy: #1f2257;
    --grey-text: #55596f;
    --card: #ffffff;
    --page: #f2f3f1;
    --smoke-light: #edf6ea;
    --smoke-mid: #bfdeb4;
  }
  * { box-sizing: border-box; margin: 0; padding: 0; }
  html, body {
    width: 1200px; height: 960px; overflow: hidden;
    background: var(--page);
  }
  .canvas {
    width: 1200px; height: 960px;
    display: flex; align-items: center; justify-content: center;
  }
  .business-card {
    position: relative;
    width: 840px; height: 480px;
    background: var(--card);
    overflow: hidden;
    box-shadow: 0 10px 40px rgba(0,0,0,0.12);
  }
  .top-band {
    position: absolute; left: 0; top: 0; right: 0; height: 40px;
    background: var(--lime);
  }
  .bottom-band {
    position: absolute; left: 0; bottom: 0; right: 0; height: 56px;
    background: var(--lime);
    display: flex; align-items: center; justify-content: flex-end;
    padding-right: 32px;
  }
  .abn {
    position: absolute; right: 32px; top: 54px;
    font-family: "Open Sans", sans-serif;
    font-size: 16px;
    color: var(--lime-dark);
  }
  .email {
    font-family: "Open Sans", sans-serif;
    font-size: 16px;
    color: var(--lime-dark);
  }
  .smoke-area {
    position: absolute; left: 0; top: 40px; width: 240px; height: 250px;
    background: radial-gradient(ellipse at 45% 35%, var(--smoke-mid) 0%, var(--smoke-light) 45%, var(--card) 78%);
  }
  .brand {
    position: absolute; left: 40px; top: 196px;
    display: flex; align-items: center; gap: 12px;
  }
  .brand-dot {
    width: 16px; height: 16px; border-radius: 50%;
    background: var(--lime);
  }
  .brand-name {
    font-family: "Crimson Text", serif;
    font-size: 34px;
    line-height: 1.05;
    letter-spacing: 0.04em;
    color: var(--navy);
  }
  .divider {
    position: absolute; left: 300px; top: 170px; width: 2px; height: 130px;
    background: var(--lime);
  }
  .contact {
    position: absolute; left: 324px; top: 176px;
  }
  .person-name {
    font-family: "Crimson Text", serif;
    font-weight: 400;
    font-size: 34px;
    color: var(--navy);
    margin-bottom: 8px;
  }
  .contact-line {
    font-family: "Open Sans", sans-serif;
    font-weight: 300;
    font-size: 17px;
    line-height: 1.5;
    color: var(--grey-text);
  }
</style>
</head>
<body>
<main class="canvas">
  <article class="business-card">
    <header class="top-band"></header>
    <p class="abn">ABN 61 904 127 558 003</p>

    <div class="smoke-area" role="img" aria-label="Soft green smoke wisps rising in the top left corner"></div>

    <div class="brand">
      <span class="brand-dot"></span>
      <span class="brand-name">BRAVELL<br>PLUMBING</span>
    </div>

    <div class="divider"></div>

    <section class="contact">
      <h1 class="person-name">Trevor Hasketh</h1>
      <p class="contact-line">Licensed Plumber 83615</p>
      <p class="contact-line">Phone: 0412 870 245</p>
      <p class="contact-line">27 Bravell Drive, Fernhollow. 3987 Westmark</p>
    </section>

    <footer class="bottom-band">
      <p class="email">Email: bravellplumbing@mailnest.example</p>
    </footer>
  </article>
</main>
</body>
</html>
```